Funding your Foodie Dreams!

I need a website design for a crowdfunding site that is 100% food/beverage oriented. Artbazaar is a crowdsourcing site and my site will be a crowdfunding site. It needs to be very clean, modern, BUT easy to use with a clear path to all critical elements.

This is the current site, that I need to fit into, http://www.grantygrove.com.hosted.pledgehostnode.com

This site, http://tinmeadow.co, is PERFECT in the fact that it does not look bland or corporate in anyway and it is beautiful and effective. My site is comparable to their "Fund" section. The photo's and ease of the site is what I would love to emulate, but my site needs to be more vibrant, fun, a happy place, which can be done with colors and textures of the site. Think of food, family, local restaurants, how you feel when you are there. I would love to have that feel just from a website.

*** These sites are some sites for competitor companies and how this site needs to operate.
boostwagon.com
mealrise.com
pledgorix.com
cashtopia.com

Here are a couple sites, that I like the look of:
us.vex.com
hopquill.com
505ladlepages.com

I would like to function like a Boostwagon but would love it to NOT look like all the rest.
Updates

I wanted to share this site, I found today.  Love the ease of the site and the look at feel but would want mine to me more fun, food, not as ... serious... but just as professional.

http://tinmeadow.co

Reason: Hello I am extending the deadline as I have yet to receive any viable designs but received some today that with some work might be the ones so please send any designs through and please send changes through quickly. I AM expecting to award this project but with the limited # of designs, might cancel it and re-issue for a far less $ amount but make it guaranteed. Thank you very much for the few designs that have been submitted to date. C

Target Market(s)

Technically savy individuals that have an entrepreneurial spirit. Individuals that will be reaching out to friends and family to use this site who will NOT be as technologically advanced and needs the site to be very clear and easy to use but not childish.

Industry/Entity Type

Crowdfunding

Font styles to use
Sans Serif

Colors
f04950
9bcb3c
ffffff
f37123
6b449b
0555a3

Requirements
Must have
• This website will be done using a white-lable platform and so I need someone that understands the limitations of that type of a platform and can work within those boundaries.

Pages Required:
Start a Campaign
Browse Campaigns
What is grantygrove?
Help
Contact

Header & Footer

Links to Social Media
Chatterbook
Chirplet
Snapvane
Clipboardly
Rambloo
Nice to have
• If you can provide any coding or direction for the coding of the design in HTML, Javascript and/or CSS, these designs will have preference.

Looking for a site that will grow from only crowdfunding to include a shopping component as well as section for campaign creators to be able to get help from service providers with their campaigns maybe a blog and a forum.
Should not have
• Do NOT provide canned websites that do not meet the Must Have's. I have to use the platform format as mentioned above as I am not have a 100% custom site developed. If these sites are provided they will be eliminated immediately.

Should not resemble a corporate site in anyway.

```html
<!DOCTYPE html>
<html lang="en">
<head>
<meta charset="utf-8">
<title>grantygrove – Funding your Foodie Dreams</title>
<link href="https://fonts.googleapis.com/css2?family=Open+Sans:wght@400;600;700&display=swap" rel="stylesheet">
<style>
:root{
  --red:#b3121c;
  --red-bright:#d3202a;
  --green:#9bcb3c;
  --ink:#333333;
  --muted:#777777;
  --line:#dddddd;
  --page:#ffffff;
  --outer:#f1f1f1;
  --footer:#2a2a2a;
  --footer-text:#b9b9b9;
}
*{box-sizing:border-box;margin:0;padding:0}
html,body{width:758px;height:1200px;overflow:hidden}
body{background:var(--outer);font-family:"Open Sans",Arial,sans-serif;color:var(--ink);position:relative}
.page{position:absolute;left:88px;top:0;width:582px;height:1092px;background:var(--page)}
.site-header{height:62px;position:relative}
.brand{position:absolute;left:8px;top:20px}
.brand-name{font-size:25px;font-weight:600;color:var(--ink);letter-spacing:-.3px}
.account-links{position:absolute;right:10px;top:8px;font-size:8px;color:var(--muted)}
.account-links span{margin:0 4px}
.main-nav{height:22px;background:var(--red);display:flex;justify-content:space-around;align-items:center;padding:0 40px}
.main-nav a{color:#fff;font-size:9.5px;text-decoration:none;text-transform:uppercase;letter-spacing:.3px}
.hero{position:relative;height:220px;margin-top:4px;background:linear-gradient(90deg,#c9a67a 0%,#e9d2b0 30%,#efe6d6 55%,#e3dccd 100%)}
.hero-text{position:absolute;left:262px;top:80px}
.hero-text h1{font-size:27px;font-weight:600;color:#3a3a3a;line-height:1.1}
.hero-text p{font-size:19px;color:#444;margin-top:2px}
.hero-arrow{position:absolute;top:98px;width:20px;height:20px;border-radius:50%;background:rgba(255,255,255,.7);display:flex;align-items:center;justify-content:center}
.hero-arrow.prev{left:8px}.hero-arrow.next{right:8px}
.section-title{font-size:15px;font-weight:600;color:var(--red-bright)}
.featured{padding:0 8px}
.featured .section-title{margin-top:18px;border-bottom:1px solid var(--line);padding-bottom:6px}
.campaign-grid{display:grid;grid-template-columns:repeat(3,178px);column-gap:16px;row-gap:18px;margin-top:14px}
.campaign{height:244px}
.campaign-photo{height:118px}
.campaign h3{font-size:9.5px;font-weight:600;margin:8px 0 4px;color:#444}
.campaign p{font-size:7px;line-height:1.45;color:var(--muted);height:40px}
.progress{height:4px;background:#e4e4e4;margin:18px 0 4px}
.progress span{display:block;height:100%;width:100%;background:var(--green)}
.stats{height:22px;background:var(--red);display:flex;color:#fff;font-size:6.5px;line-height:1.2;padding:3px 6px;gap:16px}
.stats b{display:block;font-size:7px}
.lower{display:grid;grid-template-columns:178px 178px 178px;column-gap:16px;padding:0 8px;margin-top:16px}
.lower .section-title{margin-bottom:10px}
.about-photo{height:100px}
.about p{font-size:7px;line-height:1.45;color:var(--muted);margin-top:8px}
.testimonial{border:1px solid var(--line);padding:10px;height:158px}
.testimonial-photo{width:50px;height:52px;margin:0 auto}
.testimonial p{font-size:7px;line-height:1.45;color:var(--muted);margin-top:8px;text-align:center}
.testimonial .author{text-align:right;color:var(--red-bright);font-size:7px;margin-top:6px}
.social-box{border:1px solid var(--line);padding:8px;height:150px;margin-top:6px}
.social-box h4{font-size:16px;font-weight:600;color:var(--ink)}
.social-faces{height:70px;margin-top:6px}
.cta{display:inline-block;background:var(--red-bright);color:#fff;font-size:8px;padding:4px 12px;border-radius:3px;margin-top:10px;margin-left:30px}
.site-footer{position:absolute;left:0;top:1092px;width:758px;height:108px;background:var(--footer);color:var(--footer-text)}
.footer-cols{position:absolute;left:96px;top:12px;width:566px;display:grid;grid-template-columns:130px 130px 150px 150px}
.footer-cols h5{font-size:8px;color:#fff;font-weight:600;margin-bottom:4px}
.footer-cols li{list-style:none;font-size:6.5px;line-height:1.5}
.social-icons{display:flex;gap:4px}
.social-icons span{width:12px;height:12px;border-radius:2px;background:#555}
.ready .cta{margin:4px 0 0}
.copyright{position:absolute;left:0;right:0;bottom:8px;text-align:center;font-size:6.5px}
</style>
</head>
<body>
<div class="page">
  <header class="site-header">
    <div class="brand"><span class="brand-name">grantygrove</span></div>
    <div class="account-links"><span>Create Account</span>|<span>Login</span></div>
  </header>
  <nav class="main-nav">
    <a href="#">Start a Campaign</a><a href="#">Browse</a><a href="#">Contact Us</a><a href="#">About Us</a><a href="#">Help</a>
  </nav>
  <section class="hero">
    <div role="img" aria-label="Smiling shopper carrying colourful bags" style="position:absolute;inset:0"></div>
    <div class="hero-text"><h1>Welcome to your new</h1><p>Crowdfunding platform</p></div>
    <span class="hero-arrow prev"><svg width="8" height="8" viewBox="0 0 8 8"><path d="M5.5 1 2.5 4l3 3" fill="none" stroke="#666" stroke-width="1.4"/></svg></span>
    <span class="hero-arrow next"><svg width="8" height="8" viewBox="0 0 8 8"><path d="M2.5 1l3 3-3 3" fill="none" stroke="#666" stroke-width="1.4"/></svg></span>
  </section>

  <section class="featured">
    <h2 class="section-title">Featured Campaigns</h2>
    <div class="campaign-grid">
      <article class="campaign">
        <div class="campaign-photo" role="img" aria-label="Friends shopping in the street" style="background:linear-gradient(135deg,#b9b4ac,#e8e2d8)"></div>
        <h3>Pop India a show in Goa featuring</h3>
        <p>Fresh local dishes cooked live on stage for the whole family, with tasting plates, music and stories from our kitchen team every night.</p>
        <div class="progress"><span></span></div>
        <div class="stats"><div><b>100%</b>Funded</div><div><b>$14,829</b>Pledged</div><div><b>31</b>Days to go</div></div>
      </article>
      <article class="campaign">
        <div class="campaign-photo" role="img" aria-label="Yellow sports car on a road" style="background:linear-gradient(135deg,#6e6a5c,#c9b44a)"></div>
        <h3>Pop India a show in Goa featuring</h3>
        <p>Fresh local dishes cooked live on stage for the whole family, with tasting plates, music and stories from our kitchen team every night.</p>
        <div class="progress"><span></span></div>
        <div class="stats"><div><b>100%</b>Funded</div><div><b>$14,829</b>Pledged</div><div><b>31</b>Days to go</div></div>
      </article>
      <article class="campaign">
        <div class="campaign-photo" role="img" aria-label="Hand holding a smartphone" style="background:linear-gradient(135deg,#d9c7b0,#4f7fb8)"></div>
        <h3>Pop India a show in Goa featuring</h3>
        <p>Fresh local dishes cooked live on stage for the whole family, with tasting plates, music and stories from our kitchen team every night.</p>
        <div class="progress"><span></span></div>
        <div class="stats"><div><b>100%</b>Funded</div><div><b>$14,829</b>Pledged</div><div><b>31</b>Days to go</div></div>
      </article>
      <article class="campaign">
        <div class="campaign-photo" role="img" aria-label="Family relaxing on a sofa" style="background:linear-gradient(135deg,#c8c2b6,#8a8176)"></div>
        <h3>Pop India a show in Goa featuring</h3>
        <p>Fresh local dishes cooked live on stage for the whole family, with tasting plates, music and stories from our kitchen team every night.</p>
        <div class="progress"><span></span></div>
        <div class="stats"><div><b>100%</b>Funded</div><div><b>$14,829</b>Pledged</div><div><b>31</b>Days to go</div></div>
      </article>
      <article class="campaign">
        <div class="campaign-photo" role="img" aria-label="Man in a gym with equipment" style="background:linear-gradient(135deg,#3f4650,#9aa1a8)"></div>
        <h3>Pop India a show in Goa featuring</h3>
        <p>Fresh local dishes cooked live on stage for the whole family, with tasting plates, music and stories from our kitchen team every night.</p>
        <div class="progress"><span></span></div>
        <div class="stats"><div><b>100%</b>Funded</div><div><b>$14,829</b>Pledged</div><div><b>31</b>Days to go</div></div>
      </article>
      <article class="campaign">
        <div class="campaign-photo" role="img" aria-label="Happy shopper with bags" style="background:linear-gradient(135deg,#d8b08a,#c44f6a)"></div>
        <h3>Pop India a show in Goa featuring</h3>
        <p>Fresh local dishes cooked live on stage for the whole family, with tasting plates, music and stories from our kitchen team every night.</p>
        <div class="progress"><span></span></div>
        <div class="stats"><div><b>100%</b>Funded</div><div><b>$14,829</b>Pledged</div><div><b>31</b>Days to go</div></div>
      </article>
    </div>
  </section>

  <section class="lower">
    <div class="about">
      <h2 class="section-title">About us</h2>
      <div class="about-photo" role="img" aria-label="Portrait of a businessman in a suit" style="background:linear-gradient(135deg,#8b93a0,#d8dce2)"></div>
      <p>We help food lovers turn kitchen ideas into real places, bringing friends, family and local diners together to fund every tasty dream.</p>
    </div>
    <div>
      <h2 class="section-title">Teatimonials</h2>
      <div class="testimonial">
        <div class="testimonial-photo" role="img" aria-label="Portrait of a smiling woman" style="background:linear-gradient(135deg,#c9b9a6,#eee4d8)"></div>
        <p>“Our family bakery reached its goal in three weeks. The site was simple for everyone to use and our neighbours loved sharing it.”</p>
        <div class="author">Tessa Morrow<br>16 jan 2013</div>
      </div>
    </div>
    <div>
      <div class="social-box">
        <h4>Chatterbook</h4>
        <div class="social-faces" role="img" aria-label="Grid of follower profile pictures" style="background:linear-gradient(135deg,#b7aea4,#8f8a84)"></div>
        <span class="cta">Start a campaign</span>
      </div>
    </div>
  </section>
</div>

<footer class="site-footer">
  <div class="footer-cols">
    <div><h5>Browse Campaigns</h5><ul><li>Featured Campaigns</li><li>Successful Campaigns</li><li>New Campaigns</li><li>Ending Soon</li><li>Most Funded Campaigns</li></ul></div>
    <div><h5>About</h5><ul><li>About grantygrove</li><li>Contact Us</li><li>Help</li><li>Privacy Policy</li><li>Terms Of Service</li></ul></div>
    <div><h5>Stay In Touch</h5><div class="social-icons"><span></span><span></span><span></span><span></span><span></span></div></div>
    <div class="ready"><h5>Ready to start?</h5><span class="cta">Start a campaign</span></div>
  </div>
  <div class="copyright">Copyright © grantygrove All rights reserved</div>
</footer>
</body>
</html>
```